Vorrel Sports Nutrition Brand needs a Packaging label

Hi all, please see the considerations for our vision.
We need a Golden Ratio packaging label design for new Sports nutrition/supplement brand. I would like to give you a little bit of background about myself and hopefully that will help you in creating the design.
I am myself into fitness. I am 33 years old at the moment and been hitting gyms consistently from 14 years old. I do use supplements of all types that helps with performance and body compositions.
Ideally I would like the brand to be able to resonate with male and female audience. The brand needs to give premium look and feel. Those people who will be associating themselves with the brand should be proud of themselves being a part of the team. That's our ideal customer persona.
In terms of colours we are open to your suggestions but do think that red should be included as a detail colour.
P.S Please check out my Instagram to learn more about ideal customer for the brand. @pamodeyxx
When creating the name ''vorrel'' we wanted the name to capture two things. First a feeling that we get when we go to gyms and the feeling is excited. And secondly the name for the product or the industry and that's nutrition. We then shortened the feeling excited to Vorrel for a more catchy name.

The Nutrition information will be sent to add once we pick the design.
The pictures of brands that we admire them are attached.

Please design One label design and just resize for these products. For dimensions please refer to the Print guide attached.
Bulk Core Builder 2.25KG
Tasty Creatine 250G
Vigor Lift Prime 120 Tabs
Surge Flow Pre Workout 250G
Branded Shakers

Target Market(s)

Fitness / bodybuilding audience male & female mass market

Industry/Entity Type

Nutrition

Colors

Designer to choose colors to be used in the design.

Requirements
Must have
• Our logo.
• Please find it attached
Nice to have
• The transparent Logo X some where in the background almost like a watermark. In other words like a subconscious clue.
Should not have
• Organic look.

```html
<!DOCTYPE html>
<html lang="en">
<head>
<meta charset="utf-8">
<title>Vorrel Nutrition – Vigor Lift Prime Label</title>
<link rel="stylesheet" href="https://fonts.googleapis.com/css2?family=Russo+One&family=Roboto:wght@500&display=swap">
<style>
  :root {
    --page: #ffffff;
    --blue-deep: #1f5fa8;
    --blue-mid: #2a8fd6;
    --blue-light: #5cc4ee;
    --red-deep: #8e1016;
    --red-mid: #c4161c;
    --silver-dark: #6e6f72;
    --silver-light: #e4e5e7;
    --ink: #1a1a1a;
    --gold: #f6d32a;
    --white: #ffffff;
  }
  html, body {
    margin: 0;
    padding: 0;
    width: 1200px;
    height: 1200px;
    overflow: hidden;
    background: var(--page);
  }
  .canvas {
    position: relative;
    width: 1200px;
    height: 1200px;
  }
  .label {
    position: absolute;
    left: 40px;
    top: 340px;
    width: 1120px;
    height: 520px;
    box-shadow: 0 10px 30px rgba(0,0,0,0.15);
  }
  .label svg { display: block; }
  .brand-name {
    font-family: "Russo One", sans-serif;
    font-size: 64px;
    fill: var(--ink);
    letter-spacing: 2px;
  }
  .brand-sub {
    font-family: "Roboto", sans-serif;
    font-weight: 500;
    font-size: 22px;
    letter-spacing: 9px;
    fill: var(--ink);
  }
  .product-title {
    font-family: "Russo One", sans-serif;
    fill: url(#titleFill);
    stroke: var(--white);
    stroke-width: 1.5px;
    paint-order: stroke;
  }
  .count-number {
    font-family: "Russo One", sans-serif;
    font-size: 92px;
    fill: var(--gold);
    stroke: var(--red-deep);
    stroke-width: 2px;
    paint-order: stroke;
  }
  .count-unit {
    font-family: "Russo One", sans-serif;
    font-size: 22px;
    fill: var(--gold);
    stroke: var(--red-deep);
    stroke-width: 1px;
    paint-order: stroke;
  }
</style>
</head>
<body>
<main class="canvas">
  <section class="label" aria-label="Vigor Lift Prime supplement label">
    <svg width="1120" height="520" viewBox="0 0 1120 520" xmlns="http://www.w3.org/2000/svg">
      <defs>
        <linearGradient id="blueField" x1="0" y1="0" x2="1" y2="1">
          <stop offset="0" stop-color="var(--blue-mid)"/>
          <stop offset="0.35" stop-color="var(--blue-light)"/>
          <stop offset="0.7" stop-color="var(--blue-mid)"/>
          <stop offset="1" stop-color="var(--blue-deep)"/>
        </linearGradient>
        <linearGradient id="redPanel" x1="0" y1="0" x2="1" y2="0">
          <stop offset="0" stop-color="var(--red-deep)"/>
          <stop offset="0.5" stop-color="var(--red-mid)"/>
          <stop offset="1" stop-color="var(--red-deep)"/>
        </linearGradient>
        <linearGradient id="silverBand" x1="0" y1="0" x2="0" y2="1">
          <stop offset="0" stop-color="var(--silver-light)"/>
          <stop offset="1" stop-color="var(--silver-dark)"/>
        </linearGradient>
        <linearGradient id="titleFill" x1="0" y1="0" x2="0" y2="1">
          <stop offset="0" stop-color="var(--blue-light)"/>
          <stop offset="1" stop-color="var(--blue-deep)"/>
        </linearGradient>
        <linearGradient id="countBox" x1="0" y1="0" x2="0" y2="1">
          <stop offset="0" stop-color="var(--blue-deep)"/>
          <stop offset="1" stop-color="var(--blue-mid)"/>
        </linearGradient>
        <linearGradient id="athleteTone" x1="0" y1="0" x2="0" y2="1">
          <stop offset="0" stop-color="var(--red-mid)" stop-opacity="0.85"/>
          <stop offset="1" stop-color="var(--red-deep)" stop-opacity="0.85"/>
        </linearGradient>
      </defs>

      <!-- blue field -->
      <rect class="label-field" x="0" y="0" width="1120" height="520" fill="url(#blueField)"/>

      <!-- athlete artwork area -->
      <rect class="athlete-art" role="img" aria-label="Red silhouette of a running female athlete"
            x="190" y="70" width="150" height="340" rx="40" fill="url(#athleteTone)"/>

      <!-- brand mark -->
      <g class="brand-mark" transform="translate(520 420) rotate(-90)">
        <rect x="0" y="-52" width="40" height="40" fill="var(--red-mid)"/>
        <text class="brand-name" x="56" y="-8">VORREL</text>
        <text class="brand-sub" x="56" y="28">NUTRITION</text>
      </g>

      <!-- bottom wave -->
      <path class="wave-band" d="M0 430 C 180 390, 380 400, 560 470 C 620 490, 640 480, 640 480 L640 520 L0 520 Z" fill="url(#silverBand)"/>
      <path class="wave-accent" d="M0 430 C 180 390, 380 400, 560 470 C 600 485, 630 482, 640 478" fill="none" stroke="var(--red-mid)" stroke-width="5"/>
      <path class="wave-band" d="M940 430 C 1000 415, 1060 410, 1120 412 L1120 520 L940 520 Z" fill="url(#silverBand)"/>
      <path class="wave-accent" d="M940 430 C 1000 415, 1060 410, 1120 412" fill="none" stroke="var(--red-mid)" stroke-width="5"/>

      <!-- product panel -->
      <g class="product-panel">
        <rect x="640" y="0" width="300" height="520" fill="url(#redPanel)"/>
        <rect x="640" y="0" width="6" height="520" fill="var(--blue-mid)"/>
        <rect x="934" y="0" width="6" height="520" fill="var(--blue-mid)"/>
        <text class="product-title" x="790" y="92" text-anchor="middle" font-size="74">VIGOR</text>
        <text class="product-title" x="790" y="146" text-anchor="middle" font-size="44">LIFT</text>
        <text class="product-title" x="790" y="228" text-anchor="middle" font-size="74">PRIME</text>
        <rect class="count-box" x="710" y="290" width="160" height="200" rx="14" fill="url(#countBox)"/>
        <text class="count-number" x="790" y="392" text-anchor="middle">30</text>
        <text class="count-unit" x="790" y="428" text-anchor="middle">CAPSULES</text>
      </g>
    </svg>
  </section>
</main>
</body>
</html>
```